Technology Solutions Provider

Let’s design a business card that will be as simple and bold at the same time. Name, email address, website & phone number.

Target Market(s)

Small to Medium Size Business

Industry/Entity Type

It Professional

Contact Information for Business Card

Name, email, website, phone numbers

Font styles to use
Sans Serif

Colors
ec1f27
f04a50
dddddd
919191
000000
ffffff

Requirements
Must have
• Clean simple look using my existing logo. I just need to the basic contact information on this card.
Nice to have
• Im considering the square size card versus the standard size business card.
Should not have
• No Mailing Address, no list of services.

```html
<!DOCTYPE html>
<html lang="en">
<head>
<meta charset="utf-8">
<title>Nimbus Links – Business Card</title>
<link href="https://fonts.googleapis.com/css2?family=Lato:wght@300;400;700&display=swap" rel="stylesheet">
<style>
  :root {
    --brand-red: #dc2227;
    --band-grey: #919191;
    --paper: #ffffff;
    --stage: #3a3a3a;
    --ink-light: #ffffff;
  }
  * { box-sizing: border-box; margin: 0; padding: 0; }
  html, body {
    width: 1200px; height: 900px; overflow: hidden;
    background: var(--stage);
    font-family: "Lato", Arial, sans-serif;
  }
  .canvas {
    width: 1200px; height: 900px;
    display: flex; align-items: center; justify-content: center; gap: 40px;
  }
  .card {
    width: 540px; height: 309px; position: relative; overflow: hidden;
  }
  /* Front */
  .card-front { background: var(--paper); }
  .name-block {
    position: absolute; left: 0; top: 62px; width: 190px; height: 150px;
    background: var(--brand-red); color: var(--ink-light);
    padding: 24px 0 0 20px;
  }
  .person-name { font-weight: 700; font-size: 21px; letter-spacing: -0.3px; line-height: 1.1; white-space: nowrap; }
  .person-title { font-weight: 400; font-size: 12px; margin-top: 3px; }
  .contact-block {
    position: absolute; left: 190px; right: 0; top: 112px; height: 140px;
    background: var(--band-grey); color: var(--ink-light);
    display: flex; flex-direction: column; justify-content: center;
    padding-left: 46px;
  }
  .divider {
    position: absolute; left: 20px; top: 16px; bottom: 16px; width: 1px; background: var(--ink-light);
  }
  .contact-line { display: flex; align-items: center; font-size: 14px; line-height: 1.5; white-space: nowrap; }
  .contact-line svg { width: 10px; height: 10px; margin-left: -17px; margin-right: 7px; flex: none; }
  /* Back */
  .card-back { background: var(--brand-red); color: var(--ink-light); }
  .wordmark {
    position: absolute; left: 100px; top: 92px;
    font-weight: 300; font-size: 54px; letter-spacing: 1px; line-height: 1;
  }
  .tagline {
    position: absolute; left: 186px; top: 152px;
    font-weight: 300; font-size: 15px; letter-spacing: 0.4px;
  }
  .back-web {
    position: absolute; left: 100px; top: 218px; font-size: 13px; font-weight: 400;
  }
</style>
</head>
<body>
<main class="canvas">
  <section class="card card-front">
    <div class="name-block">
      <p class="person-name">Daniel Okafor</p>
      <p class="person-title">Manager</p>
    </div>
    <div class="contact-block">
      <span class="divider"></span>
      <p class="contact-line">
        <svg viewBox="0 0 10 10" aria-hidden="true"><path d="M2 0.5 L4 2.5 L3 3.8 Q4.5 6 6.2 7 L7.5 6 L9.5 8 L8 9.5 Q2 8.5 0.5 2 Z" fill="var(--brand-red)"/></svg>
        512 555 0147</p>
      <p class="contact-line">
        <svg viewBox="0 0 10 10" aria-hidden="true"><rect x="0.5" y="2" width="9" height="6.5" fill="var(--brand-red)"/><path d="M0.5 2 L5 5.8 L9.5 2" stroke="#fff" stroke-width="0.8" fill="none"/></svg>
        info@nimbuslinks.com</p>
      <p class="contact-line">
        <svg viewBox="0 0 10 10" aria-hidden="true"><circle cx="5" cy="5" r="4.5" fill="var(--brand-red)"/><path d="M0.5 5 H9.5 M5 0.5 V9.5 M1.5 3 H8.5 M1.5 7 H8.5" stroke="#fff" stroke-width="0.6"/></svg>
        www.nimbuslinks.com</p>
    </div>
  </section>

  <section class="card card-back">
    <p class="wordmark">nimbus links</p>
    <p class="tagline">technology solutions provider</p>
    <p class="back-web">www.nimbuslinks.com</p>
  </section>
</main>
</body>
</html>
```